Zippy Festivities!!! New business idea looking for proof of concept among customers

PERSONAL, FUN, EXCITING, MEMORABLE, UNIQUE
this is the idea for the business so I would like the brochure to portray this as well
I would like an eye catching design. The concept of the business is simple. We want to provide a personalized, memorable, unique and enjoyable experience and celebration for our clients as they chose to celebrate different events which may include but are not limited to (Birthday, holiday, anniversary, Special Event, no reason) for whomever it may be (friend, family member, significant other, coworker, frat/sorority brother/sister, etc) at a location of their choosing (on campus, public park, restaurant, bar etc). The celebration can take place at a private location or in a public scene where strangers can look on and take part in the fun. We will catch this act on video as well as take personalized photos and share it with the client for their own personal memories as well as utilize it on our own social media platforms. There are different packages that i would like to be included and most of the information id like to be included is attached. However, I would like to be able to add information or discard as necessary. The logo I would like to use is attached as well in three different designs. Designers may utilize the logo that they see fits their personal design the best! the logo with the flash in the background is one I personally like most but I am open to anything.
Just for visual of the concept. you want to surprise your friend with a Birthday blowout package for their birthday. The two of you are walking to class when your friend is shouted out by a DJ using a portable pa speaker system. Suddenly two confetti cannons go off, and your friend is overwhelmed with attention as well as personalized gifts given by strangers. Your friend as well as all onlookers are baffled to learn that you set up the whole experience just for them. Photos and videos have been taken throughout the whole experience to be shared with friends who weren't able to be their in person.
Designers you have the opportunity to be a part of a new, exciting and fun business. More than likely I will need a lot of things designed for the future of this business and I am looking to potentially develop a long-term partnership.
Target Market(s)
Ages 18-35. College students, Couples, office workers. Anybody celebrating anything.
Industry/Entity Type
Business
Requirements
Must have
- visuals that capture the attention of those viewing the brochure as well as providing a clear explanation of the concepts and packages. Packages must be easy to edit as pricing is not finalized. I would like the different packages to be on different pages with corresponding pictures in the panels or as background that still fit the overall theme. When you open the brochure the three panels should be Birthdays, Anniversaries, Other events, each with corresponding information from attached document

```html
<!DOCTYPE html>
<html lang="en">
<head>
<meta charset="utf-8">
<title>Zippy Festivities – Birthday Packages</title>
<link href="https://fonts.googleapis.com/css2?family=Cinzel+Decorative:wght@700&family=Great+Vibes&family=Lato:ital,wght@0,400;0,700;1,400&family=Merriweather:wght@700&display=swap" rel="stylesheet">
<style>
  :root{
    --cream:#f3ecdc;
    --cream-light:#fbf7ee;
    --navy:#1d1f6b;
    --navy-deep:#13155a;
    --royal:#2a3fa0;
    --purple-ink:#3d3a8e;
    --yellow:#f3f36a;
    --cyan:#56d9f0;
    --red:#d2161d;
    --text:#2b2b3a;
    --frame:#f4f6a8;
  }
  *{box-sizing:border-box;margin:0;padding:0}
  html,body{width:848px;height:1200px;overflow:hidden;background:var(--cream)}
  .flyer{
    position:relative;width:848px;height:1200px;overflow:hidden;
    background:radial-gradient(ellipse at 50% 35%, var(--cream-light) 0%, var(--cream) 55%, #e6dcc5 100%);
    font-family:"Lato",sans-serif;color:var(--text);
  }
  .brand{
    position:absolute;top:58px;left:0;width:100%;text-align:center;
    font-family:"Cinzel Decorative",serif;font-weight:700;color:var(--purple-ink);
    line-height:1.05;
  }
  .brand .line1{display:block;font-size:92px;letter-spacing:6px}
  .brand .line2{display:block;font-size:62px;letter-spacing:2px}
  .balloons{position:absolute;width:170px;height:210px;
    background:radial-gradient(circle at 55% 30%, #29a9ea 0 28%, transparent 29%),
               radial-gradient(circle at 30% 70%, #e23b2c 0 24%, transparent 25%);}
  .balloons.left{left:0;top:220px}
  .balloons.right{right:0;top:220px}
  .photo{position:absolute;border:6px solid var(--frame);background:var(--navy);padding:10px}
  .photo .fill{width:100%;height:100%}
  .photo.gift{left:34px;top:460px;width:190px;height:190px;transform:rotate(-9deg)}
  .photo.gift .fill{background:linear-gradient(160deg,#f5f5f5,#3c78c8 60%,#c8a24a)}
  .photo.cake{left:620px;top:450px;width:200px;height:190px;transform:rotate(8deg)}
  .photo.cake .fill{background:linear-gradient(160deg,#3a8fb8,#f2efe8 60%,#e6b94d)}
  .photo.friends{left:185px;top:312px;width:446px;height:284px;transform:rotate(-2deg);z-index:2}
  .photo.friends .fill{background:linear-gradient(135deg,#c9b08f,#e7c3a8 45%,#6b4a3a 80%)}
  .greeting{
    position:absolute;left:0;top:596px;width:100%;height:205px;z-index:3;
    background:radial-gradient(ellipse at 60% 40%, var(--royal) 0%, var(--navy) 55%, var(--navy-deep) 100%);
  }
  .greeting h1{
    position:absolute;left:70px;top:18px;
    font-family:"Great Vibes",cursive;font-weight:400;font-size:106px;color:var(--yellow);
  }
  .greeting .dear{
    position:absolute;left:470px;top:120px;
    font-family:"Great Vibes",cursive;font-size:50px;color:var(--cyan);
  }
  .greeting .dear-line{position:absolute;left:630px;top:157px;width:140px;height:2px;background:var(--cyan)}
  .packages-title{
    position:absolute;top:816px;left:0;width:100%;text-align:center;
    font-family:"Great Vibes",cursive;font-size:34px;color:var(--navy);
  }
  .bottom-band{position:absolute;left:0;bottom:0;width:100%;height:49px;
    background:linear-gradient(90deg,var(--navy-deep),var(--royal) 50%,var(--navy-deep))}
  .card{
    position:absolute;top:871px;width:252px;height:294px;z-index:2;
    background:var(--cream-light);border-radius:14px;
    box-shadow:0 0 0 3px #efe6d2, 0 2px 6px rgba(0,0,0,.15);
    padding:50px 14px 10px 16px;
  }
  .card.basic{left:44px}
  .card.better{left:305px}
  .card.blowout{left:565px}
  .card .label{
    position:absolute;top:10px;left:50%;transform:translateX(-50%);white-space:nowrap;
    background:var(--red);color:#fff;font-family:"Merriweather",serif;font-weight:700;
    font-size:13px;padding:4px 12px;
  }
  .card ul{list-style:none}
  .card li{position:relative;padding-left:14px;font-size:11px;line-height:1.3;margin-bottom:5px}
  .card li::before{content:"";position:absolute;left:0;top:5px;width:5px;height:5px;border-radius:50%;background:var(--navy)}
  .card li.note{padding-left:24px;margin-bottom:4px}
  .card li.note::before{content:"*";background:none;color:var(--red);left:18px;top:0;width:auto;height:auto}
  .card em{font-style:italic}
</style>
</head>
<body>
<main class="flyer">
  <div class="balloons left" role="img" aria-label="Blue and red party balloons"></div>
  <div class="balloons right" role="img" aria-label="Blue and red party balloons"></div>

  <header class="brand"><span class="line1">ZIPPY</span><span class="line2">Festivities</span></header>

  <div class="photo gift"><div class="fill" role="img" aria-label="Photo of a wrapped blue gift box with a bow"></div></div>
  <div class="photo cake"><div class="fill" role="img" aria-label="Photo of a birthday cake with lit candles"></div></div>
  <div class="photo friends"><div class="fill" role="img" aria-label="Photo of friends celebrating around a birthday cake"></div></div>

  <section class="greeting">
    <h1>Happy Birthday</h1>
    <span class="dear">My Dear</span>
    <span class="dear-line"></span>
  </section>

  <h2 class="packages-title">Birthday Packages (Requires Additional Fee's)</h2>

  <article class="card basic">
    <span class="label">Basic Birthday ($99.99)</span>
    <ul>
      <li>DJ Shout out + Music <em>(to Birthday Boy/Girl including any special requests)</em></li>
      <li>Confetti <em>(Streamers exploded through confetti cannon)</em></li>
      <li>One Dozen Balloons/or One Dozen Flowers</li>
      <li>Optional: Gift Presentation</li>
      <li class="note">Photos/Videos <em>(<b>$5.00</b> per Photo/ <b>$10.00</b> Video/<b>$49.99</b> Custom Video)</em></li>
      <li class="note">Delivery Method <em>(See Options)</em></li>
      <li class="note">Additional instructions <em>(Not Listed, Fees May Vary)</em></li>
    </ul>
  </article>

  <article class="card better">
    <span class="label">Better Birthday ($124.99)</span>
    <ul>
      <li>DJ Shout out + Music <em>(to Birthday Boy/Girl including any special requests)</em></li>
      <li>Confetti <em>(Streamers exploded through confetti cannon)</em></li>
      <li>One Dozen Balloons/or One Dozen Flowers</li>
      <li>Custom Birthday Cookie Cake <em>(Sweet Harbor Cookies)</em>/ Birthday Sash &amp; Hat or Tiara</li>
      <li>Optional: Gift Presentation</li>
      <li class="note">Photos/Videos <em>(<b>$5.00</b> per Photo/ <b>$10.00</b> Video/<b>$49.99</b> Custom Video)</em></li>
      <li class="note">Delivery Method <em>(See Options)</em></li>
      <li class="note">Additional instructions <em>(Not Listed, Fees May Vary)</em></li>
    </ul>
  </article>

  <article class="card blowout">
    <span class="label">Birthday Blowout ($199.99)</span>
    <ul>
      <li>DJ Shout out + Music <em>(to Birthday Boy/Girl including any special requests)</em></li>
      <li>Confetti <em>(Streamers exploded through confetti cannon)</em></li>
      <li>One Dozen Balloons/ or One Dozen Flowers</li>
      <li>Custom Birthday Cookie Cake <em>(Sweet Harbor Cookies)</em></li>
      <li>Birthday Sash &amp; Hat/Tiara</li>
      <li>Free access to all Photos/Videos</li>
      <li>Choice of Delivery Method From Options</li>
      <li>Optional: Gift Presentation</li>
      <li class="note">Custom Delivery <em>(Not included in Options)</em></li>
      <li class="note">Additional instructions <em>(Not Listed)</em></li>
    </ul>
  </article>

  <div class="bottom-band"></div>
</main>
</body>
</html>
```